Recipe Card Design

I have a small kitchen store in Livingston Montana, and I would like to have recipe cards (4x6 postcard) designed with my logo, lines for recipe writing, all in black and white. My website is here: www.copperladlehouse.com

Store

```html
<!DOCTYPE html>
<html lang="en">
<head>
<meta charset="utf-8">
<title>Recipe Card</title>
<link rel="stylesheet" href="https://fonts.googleapis.com/css2?family=Montserrat:wght@500;600&family=Pinyon+Script&display=swap">
<style>
  :root {
    --ink: #111111;
    --paper: #ffffff;
  }
  html, body {
    margin: 0;
    padding: 0;
    overflow: hidden;
    background: var(--paper);
  }
  .card {
    position: relative;
    width: 1200px;
    height: 800px;
    background: var(--paper);
    color: var(--ink);
    overflow: hidden;
  }
  .rules {
    position: absolute;
    inset: 0;
  }
  .rules line { stroke: var(--ink); stroke-width: 1.4; }
  .rules rect.info-box { fill: none; stroke: var(--ink); stroke-width: 1; }
  .rules .icon { fill: var(--ink); }

  .title-script {
    position: absolute;
    left: 40px;
    top: -6px;
    margin: 0;
    font-family: "Pinyon Script", cursive;
    font-weight: 400;
    font-size: 118px;
    line-height: 1.3;
  }
  .title-for {
    position: absolute;
    left: 324px;
    top: 130px;
    font-family: "Montserrat", sans-serif;
    font-weight: 500;
    font-size: 37px;
    line-height: 1;
  }
  .section-heading {
    position: absolute;
    top: 190px;
    margin: 0;
    font-family: "Pinyon Script", cursive;
    font-weight: 400;
    font-size: 40px;
    line-height: 1.2;
  }
  .section-heading.ingredients { left: 58px; }
  .section-heading.instructions { left: 428px; }

  .info-label {
    position: absolute;
    left: 1035px;
    font-family: "Montserrat", sans-serif;
    font-weight: 600;
    font-size: 20px;
    line-height: 27px;
    letter-spacing: 0.2px;
  }
  .info-label.serves { top: 214px; }
  .info-label.cooking { top: 340px; }
  .info-label.oven { top: 464px; }

  .store-mark {
    position: absolute;
    left: 1022px;
    top: 610px;
    width: 145px;
    display: flex;
    flex-direction: column;
    align-items: center;
    gap: 10px;
  }
  .store-mark .mark-square {
    width: 70px;
    height: 70px;
    background: var(--ink);
  }
  .store-mark .store-name {
    font-family: "Montserrat", sans-serif;
    font-weight: 600;
    font-size: 20px;
    line-height: 24px;
    text-align: center;
    letter-spacing: 0.5px;
  }

  .web-address {
    position: absolute;
    left: 429px;
    top: 761px;
    font-family: "Montserrat", sans-serif;
    font-weight: 500;
    font-size: 17px;
    letter-spacing: 2.1px;
    line-height: 1;
  }
</style>
</head>
<body>
<main class="card">
  <svg class="rules" width="1200" height="800" viewBox="0 0 1200 800" aria-hidden="true">
    <!-- kitchen icons -->
    <g class="icon">
      <!-- pot -->
      <rect x="64" y="146" width="32" height="15" rx="3"/>
      <rect x="60" y="147" width="40" height="3"/>
      <rect x="76" y="141" width="8" height="3" rx="1"/>
      <rect x="60" y="163" width="40" height="1.5"/>
      <!-- cloche -->
      <path d="M102 159 A20 18 0 0 1 142 159 Z"/>
      <circle cx="122" cy="141" r="2"/>
      <rect x="100" y="161" width="44" height="2"/>
      <!-- cup -->
      <path d="M148 141 H170 V155 Q170 160 165 160 H153 Q148 160 148 155 Z"/>
      <path d="M170 145 H176 Q178 145 178 147 V151 Q178 153 176 153 H170 V151 H176 V147 H170 Z"/>
      <rect x="146" y="162" width="36" height="1.5"/>
    </g>

    <!-- title lines -->
    <line x1="430" y1="97" x2="1164" y2="97"/>
    <line x1="430" y1="130" x2="1164" y2="130"/>
    <line x1="430" y1="164" x2="1164" y2="164"/>

    <!-- ingredient lines -->
    <g class="ingredient-lines">
      <line x1="59" y1="262" x2="379" y2="262"/>
      <line x1="59" y1="295" x2="379" y2="295"/>
      <line x1="59" y1="330" x2="379" y2="330"/>
      <line x1="59" y1="362" x2="379" y2="362"/>
      <line x1="59" y1="395" x2="379" y2="395"/>
      <line x1="59" y1="430" x2="379" y2="430"/>
      <line x1="59" y1="462" x2="379" y2="462"/>
      <line x1="59" y1="495" x2="379" y2="495"/>
      <line x1="59" y1="530" x2="379" y2="530"/>
      <line x1="59" y1="562" x2="379" y2="562"/>
      <line x1="59" y1="595" x2="379" y2="595"/>
      <line x1="59" y1="630" x2="379" y2="630"/>
      <line x1="59" y1="669" x2="379" y2="669"/>
      <line x1="59" y1="702" x2="379" y2="702"/>
      <line x1="59" y1="737" x2="379" y2="737"/>
    </g>

    <!-- instruction lines -->
    <g class="instruction-lines">
      <line x1="430" y1="262" x2="996" y2="262"/>
      <line x1="430" y1="295" x2="996" y2="295"/>
      <line x1="430" y1="330" x2="996" y2="330"/>
      <line x1="430" y1="362" x2="996" y2="362"/>
      <line x1="430" y1="395" x2="996" y2="395"/>
      <line x1="430" y1="430" x2="996" y2="430"/>
      <line x1="430" y1="462" x2="996" y2="462"/>
      <line x1="430" y1="495" x2="996" y2="495"/>
      <line x1="430" y1="530" x2="996" y2="530"/>
      <line x1="430" y1="562" x2="996" y2="562"/>
      <line x1="430" y1="595" x2="996" y2="595"/>
      <line x1="430" y1="630" x2="996" y2="630"/>
      <line x1="430" y1="669" x2="996" y2="669"/>
      <line x1="430" y1="702" x2="996" y2="702"/>
      <line x1="430" y1="737" x2="996" y2="737"/>
    </g>

    <!-- info boxes -->
    <rect class="info-box" x="1031.5" y="211.5" width="133" height="117"/>
    <rect class="info-box" x="1031.5" y="336.5" width="133" height="117"/>
    <rect class="info-box" x="1031.5" y="460.5" width="133" height="117"/>
  </svg>

  <h1 class="title-script">Receipe</h1>
  <div class="title-for">FOR</div>

  <h2 class="section-heading ingredients">Ingredients</h2>
  <h2 class="section-heading instructions">Instructions</h2>

  <div class="info-label serves">SERVES</div>
  <div class="info-label cooking">COOKING<br>TIME</div>
  <div class="info-label oven">OVEN<br>TEMP.</div>

  <div class="store-mark">
    <div class="mark-square"></div>
    <div class="store-name">COPPER LADLE HOUSE</div>
  </div>

  <div class="web-address">www.copperladlehouse.com</div>
</main>
</body>
</html>
```